Stonebell Inc Ad Design, trying to attract new customers

Please see attached pictures and files for information
We are a Class A - Residential General Contractor in Lynchburg, VA with Master HVAC and Master PLUMBING Licenses. We focus on Water and Air Solutions for property owners.
We build, remodel, and repair homes
We do HVAC, including Humidity Control and Air Purification
We do Plumbing
We love to fix Water Leaks for Plumbing, Roof Leaks, Skylight Leaks, Basement Leaks, Foundation Leaks, Door and Window Leaks
We solve water and air issues on the outside of properties with custom structures, grading, and landscaping

Target Market(s)

Residential and Light Commercial property owners

Industry/Entity Type

Construction

Font styles to use
Other font styles liked:
• see cards

Colors
0054AA
0677BA
7BADD7
CADEEF
E8F1F8
00AB8E
00BBA5
67D7C9
C6EFE9
E9F9F6

Requirements
Must have
• See business cards
Nice to have
• see business cards
Should not have
• My name

```html
<!DOCTYPE html>
<html lang="en">
<head>
<meta charset="utf-8">
<title>Stonebell Inc – Billboard Ad</title>
<link rel="stylesheet" href="https://fonts.googleapis.com/css2?family=Saira+Condensed:wght@600;800&family=Arimo:wght@400&display=swap">
<style>
  :root {
    --page-bg: #9b9b9b;
    --navy: #0a5a94;
    --blue: #1b78c0;
    --green: #1f8a3c;
    --ink: #1b1b1b;
    --white: #ffffff;
  }
  * { box-sizing: border-box; margin: 0; padding: 0; }
  html, body { width: 933px; height: 1200px; overflow: hidden; }
  body {
    background: var(--page-bg);
    display: flex;
    align-items: center;
    justify-content: center;
    font-family: "Arimo", Arial, sans-serif;
  }
  .billboard {
    position: relative;
    width: 873px;
    height: 454px;
    background: var(--white);
    overflow: hidden;
    box-shadow: 6px 8px 10px rgba(0,0,0,.35);
  }
  .backdrop { position: absolute; inset: 0; width: 100%; height: 100%; }
  .headline {
    position: absolute;
    font-family: "Saira Condensed", "Arial Narrow", sans-serif;
    font-weight: 800;
    color: var(--navy);
    line-height: 1;
    font-size: 52px;
    letter-spacing: .5px;
    white-space: nowrap;
  }
  .headline--slogan { top: 18px; left: 84px; }
  .headline--trade { top: 76px; left: 176px; }
  .contact {
    position: absolute;
    right: 330px;
    top: 196px;
    text-align: right;
    font-family: "Saira Condensed", "Arial Narrow", sans-serif;
  }
  .contact__phone { font-weight: 800; font-size: 47px; color: var(--navy); line-height: 1; }
  .contact__email { font-weight: 600; font-size: 17px; color: var(--green); margin-top: 2px; }
  .contact__web { font-weight: 600; font-size: 22px; color: var(--green); margin-top: 18px; line-height: 1.1; }
  .contact__licence { font-weight: 600; font-size: 22px; color: var(--green); line-height: 1.2; }
  .divider {
    position: absolute;
    left: 566px; top: 179px;
    width: 2px; height: 167px;
    background: var(--blue);
  }
  .services {
    position: absolute;
    left: 589px; top: 187px;
    list-style: none;
    font-size: 13px;
    line-height: 19.4px;
    color: var(--ink);
  }
  .services li::before { content: "-"; display: inline-block; width: 13px; }
  .brand {
    position: absolute;
    left: 24px; top: 240px;
    display: flex; align-items: center; gap: 6px;
    font-family: "Saira Condensed", "Arial Narrow", sans-serif;
    font-weight: 800;
    font-size: 22px;
    letter-spacing: 1px;
    color: var(--blue);
  }
  .brand__dot { width: 14px; height: 14px; border-radius: 50%; background: var(--blue); }
  .scripture {
    position: absolute;
    left: 23px; right: 20px;
    color: var(--white);
    font-size: 12.6px;
    line-height: 17px;
  }
  .scripture__ref { top: 336px; }
  .scripture__verse { top: 370px; }
</style>
</head>
<body>
  <main class="billboard">
    <svg class="backdrop" viewBox="0 0 873 454" role="img" aria-label="Illustration of a large green tree whose trunk becomes a blue river flowing into the footer band">
      <defs>
        <linearGradient id="scene-fill" x1="0" y1="0" x2="0" y2="1">
          <stop offset="0" stop-color="#b7dd8e"/>
          <stop offset=".5" stop-color="#8fcf8a"/>
          <stop offset="1" stop-color="#7cc3ec"/>
        </linearGradient>
        <linearGradient id="scene-fade" x1="0" y1="0" x2="1" y2="0">
          <stop offset="0" stop-color="#fff" stop-opacity="1"/>
          <stop offset=".55" stop-color="#fff" stop-opacity=".8"/>
          <stop offset="1" stop-color="#fff" stop-opacity="0"/>
        </linearGradient>
        <mask id="scene-mask">
          <rect x="0" y="0" width="424" height="365" fill="url(#scene-fade)"/>
        </mask>
        <linearGradient id="band-fill" x1="0" y1="0" x2="1" y2="0">
          <stop offset="0" stop-color="#1e6fb8"/>
          <stop offset="1" stop-color="#1b78c0"/>
        </linearGradient>
      </defs>
      <rect class="scene" x="0" y="0" width="424" height="365" fill="url(#scene-fill)" mask="url(#scene-mask)"/>
      <path class="band" fill="url(#band-fill)"
            d="M0 336 C 120 322, 240 322, 330 352 C 360 362, 380 365, 420 365 L873 365 L873 454 L0 454 Z"/>
    </svg>

    <h1 class="headline headline--slogan">“WE PUT WATER AND AIR IN ITS PLACE”</h1>
    <h2 class="headline headline--trade">CLASS A RBC PLUMBING HVAC</h2>

    <div class="brand">
      <span class="brand__dot"></span>
      <span class="brand__name">STONEBELL</span>
    </div>

    <div class="contact">
      <p class="contact__phone">(434) 555-0172</p>
      <p class="contact__email">contact@StonebellVA.com</p>
      <p class="contact__web">www.BuiltOnStoneVS.com</p>
      <p class="contact__licence">Licensed and Insured</p>
    </div>

    <div class="divider"></div>

    <ul class="services">
      <li>Humidity Control/Air Purificatin</li>
      <li>Roof/Skylight Leaks</li>
      <li>Basement/Foundation Leaks</li>
      <li>Drainage/Grading/Landscaping</li>
      <li>Custom Outdoor Structures - Porches</li>
      <li>Decks</li>
      <li>Sunrooms</li>
      <li>Gazebos</li>
    </ul>

    <p class="scripture scripture__ref">PSALM 1:1-3</p>
    <p class="scripture scripture__verse">Blessed is the man who walks not in the counsel of the ungodly, nor stands in the path of sinners, nor sits in the seat of the scornful; but his delight is in the law of the Lord, and in His law he meditates day and night. He shall be like a tree planted by the rivers of water, that brings forth fruit in it’s season, whose leaf shall not wither, and whatever he does shall prosper.</p>
  </main>
</body>
</html>
```